Website for Brief Morning Rambles who develops hiking guides for easy to moderate hikes of up to 4 hours

Website for a company who creates hiking guides for State Parks and other tourist destinations. Looking for the ability to showcase various hiking destinations, our hiking guides, product favorites and blog with the ability to sell our hiking guides via the website shopping cart. Should feature photos from our hiking guides with the the ability to include photo thumbnails that can be expanded.

We need the ability to self manage the website - including ability to self update, add pages, graphics, etc.

While we want to have high quality photos we still want the pages to load quickly

Target Market(s)

People who enjoy nature and like to walk or hike for up to half a day on trails in a specific destination.
Adventure travelers who loves nature and the outdoors

Industry/Entity Type

Travel

Font styles to use
Sans Serif

Colors

Designer to choose colors to be used in the design.

Requirements
Must have
• We are looking for a fully operational WIX design for www.briefmorningrambles.example that has the following:
• 1. Menus - We want the ability to have multiple drop-down menus.
• 2. E-commerce – the ability to accept orders for books that we publish.
• 3. A form that can be filled out online to provide feedback on our hiking guides. (We will give the fields that need to be filled out.)
• 4. Pictures - Incorporates Professional Pictures– thumbnails that can be clicked to be larger, and pictures included with copy.
• 5. Logo – Our logo can be provided.
• 6. Domain Name - We already have the domain name briefmorningrambles.example
• 7. We want to be able to take your design and do our own changes via WIX.
• 8. The home page should have the ability to have scrolling photos – up to 10 images that can be easily updated.
• 9. Password protected pages that can only be accessed by a password.
• 10. We have a color palate that should be used for the site design
• 11. Six (6) major tabs
• #1 Home Page – Scrolling photos, general overview, hiking guide summary, other
• # 2 Destinations – Summary of all guides published, with sub-pages on each guide
• #3 Favorite products
• # 4 Blog – Blog index and all blogs
• #5 Photography
• #6 Contact us – form for feedback, links to other sites etc.
• We also need the ability to link to our Facebook and Instagram Accounts.
• Photos included as an example for our Home page.
• Please use the colors in our color palette provided as an attachment
Nice to have
• Examples of website designs we like as a reference
• https://www.roamingwithpelts.example
• https://www.crestvoyage.example/index.php
Should not have
• Colors that do not align with our color palette that is included as an attachment.

```html
<!DOCTYPE html>
<html lang="en">
<head>
<meta charset="utf-8">
<title>Brief Morning Rambles</title>
<link rel="stylesheet" href="https://fonts.googleapis.com/css2?family=IBM+Plex+Sans:wght@400;500;600;700&family=Open+Sans:wght@400;600;700&display=swap">
<style>
:root{
  --navy:#1e3560;
  --orange:#d4532f;
  --tile-orange:#d9552f;
  --tile-blue:#2d5ca0;
  --tile-red:#7a2a20;
  --tile-amber:#e09a3a;
  --grey-band:#f0efed;
  --blog-band:#f5f1f1;
  --text:#333;
  --line:#d9d9d9;
  --white:#fff;
}
*{box-sizing:border-box;margin:0;padding:0}
html,body{width:1200px;height:4831px;overflow:hidden}
body{font-family:"Open Sans",sans-serif;color:var(--text);background:var(--white);position:relative}
.heading-font{font-family:"IBM Plex Sans",sans-serif}
section,header,footer{position:relative;width:1200px}
.abs{position:absolute}
.btn{position:absolute;background:var(--orange);color:var(--white);font-family:"IBM Plex Sans",sans-serif;font-weight:700;text-transform:uppercase;display:flex;align-items:center;justify-content:center;letter-spacing:.3px}
.section-mark{position:absolute;left:50%;width:22px;height:22px;margin-left:-11px;background:var(--orange);transform:rotate(45deg)}
.section-title{position:absolute;left:0;width:1200px;text-align:center;font-family:"IBM Plex Sans",sans-serif;font-weight:700;color:var(--navy);font-size:29px;letter-spacing:.5px}

/* hero */
.hero{height:651px;background:linear-gradient(180deg,#7ea7c9 0%,#b9cfe0 30%,#d9e3ea 45%,#8d8a86 65%,#6b4a34 100%)}
.brand{left:130px;top:62px;font-family:"IBM Plex Sans",sans-serif;font-weight:700;color:var(--navy);font-size:22px;display:flex;align-items:center;gap:10px}
.brand-square{width:16px;height:16px;background:var(--orange)}
.main-nav{left:398px;top:64px;display:flex;gap:30px;font-family:"IBM Plex Sans",sans-serif;font-weight:600;font-size:13px;color:var(--navy)}
.cart{left:1024px;top:20px}
.cart-badge{left:1047px;top:16px;width:18px;height:18px;border-radius:50%;background:var(--orange);color:#fff;font-size:10px;font-weight:700;display:flex;align-items:center;justify-content:center}
.hero-panel{left:652px;top:281px;width:418px;height:176px;background:rgba(255,255,255,.55)}
.hero-title{left:687px;top:300px;font-family:"IBM Plex Sans",sans-serif;font-weight:700;font-size:44px;color:var(--navy);letter-spacing:1px}
.hero-sub{left:690px;top:354px;font-family:"IBM Plex Sans",sans-serif;font-weight:600;font-size:16px;color:var(--navy)}
.hero-dots{left:545px;top:591px;display:flex;gap:15px}
.hero-dots span{width:10px;height:10px;border-radius:50%;background:#fff}
.hero-dots span.active{background:var(--orange);box-shadow:0 0 0 2px #fff}

/* welcome */
.welcome{height:558px}
.welcome-photo{left:129px;top:48px;width:514px;height:445px;background:linear-gradient(180deg,#3f8fd8 0%,#9fc6e6 35%,#6f9a4a 60%,#4c7a2a 100%)}
.welcome-mark{left:688px;top:54px;width:20px;height:20px;background:var(--orange);transform:rotate(45deg)}
.welcome-kicker{left:686px;top:115px;font-family:"IBM Plex Sans",sans-serif;font-size:25px;color:var(--navy)}
.welcome-title{left:686px;top:150px;font-family:"IBM Plex Sans",sans-serif;font-weight:700;font-size:34px;color:var(--navy)}
.welcome-rule{left:688px;top:205px;width:84px;height:2px;background:var(--navy)}
.welcome-copy{left:686px;top:241px;width:385px;font-size:14.5px;line-height:22px;color:#444}

/* guides */
.guides{height:619px;background:var(--grey-band)}
.card{position:absolute;background:#fff;border:2px solid #e2e2e2}
.cover{position:absolute;left:50%;transform:translateX(-50%);box-shadow:4px 4px 8px rgba(0,0,0,.25)}
.card-name{position:absolute;font-family:"IBM Plex Sans",sans-serif;font-weight:700;color:var(--navy);font-size:16px;text-transform:uppercase}
.card-copy{position:absolute;font-size:12.5px;line-height:19px;color:#444}
.arrow{position:absolute}

/* products */
.products{height:707px}
.price{position:absolute;left:0;width:100%;text-align:center;font-family:"IBM Plex Sans",sans-serif;font-weight:700;font-size:25px;color:var(--navy)}

/* blog */
.blog{height:799px;background:var(--blog-band)}
.blog-intro{left:240px;top:164px;width:720px;text-align:center;font-size:13px;line-height:25px;color:#555}
.blog-grid{left:141px;top:328px;width:912px;height:416px;display:grid;grid-template-columns:repeat(4,228px);grid-template-rows:repeat(2,208px)}
.tile-text{color:#fff;text-align:center;padding:26px 20px 0}
.tile-text h3{font-family:"Open Sans",sans-serif;font-weight:400;font-size:20px}
.tile-text .date{font-size:14px;margin:12px 0 10px}
.tile-text p{font-size:10.5px;line-height:22px}
.tile-orange{background:var(--tile-orange)}
.tile-blue{background:var(--tile-blue)}
.tile-red{background:var(--tile-red)}
.tile-amber{background:var(--tile-amber)}

/* gallery */
.gallery{height:759px}
.thumb{position:absolute;width:298px;height:242px;border:1px solid var(--line);background:#fff;padding:7px}
.thumb div{width:100%;height:100%}

/* contact */
.contact{height:625px;background:linear-gradient(90deg,#d9dbdf 0%,#eceef0 35%,#f2f3f4 60%,#e6e8eb 100%)}
.field{position:absolute;left:377px;width:444px;background:#fff;border:1px solid #cfcfcf;font-size:12px;color:#444;padding:14px 20px;text-transform:uppercase}
.submit{left:377px;top:516px;width:444px;height:60px;font-size:24px}

/* footer */
.site-footer{height:113px;background:var(--navy);color:#fff}
.copyright{left:129px;top:50px;font-size:12px}
.follow{left:887px;top:44px;display:flex;align-items:center;gap:12px;font-size:11px}
.social{width:24px;height:24px;border-radius:50%}
</style>
</head>
<body>

<header class="hero">
  <div class="abs" role="img" aria-label="Hiker with a backpack standing on a rocky ledge facing snowy mountain peaks" style="inset:0"></div>
  <div class="abs brand"><span class="brand-square"></span>Brief Morning Rambles</div>
  <nav class="abs main-nav">
    <span>HOME</span><span>DESTINATIONS</span><span>FAVORITE PRODUCTS</span><span>BLOG</span><span>PHOTOGRAPHY</span><span>CONTACT US</span>
  </nav>
  <svg class="abs cart" width="34" height="30" viewBox="0 0 34 30" aria-label="Shopping cart">
    <path d="M2 4h6l4 16h16l3-11H10" fill="none" stroke="var(--navy)" stroke-width="2.4"/>
    <circle cx="14" cy="25" r="2.5" fill="var(--navy)"/><circle cx="26" cy="25" r="2.5" fill="var(--navy)"/>
  </svg>
  <div class="abs cart-badge">0</div>
  <div class="abs hero-panel"></div>
  <div class="abs hero-title">HIKING GUIDES</div>
  <div class="abs hero-sub">LOREM IPSUM IS SIMPLY DUMMY TEXT</div>
  <div class="btn" style="left:688px;top:392px;width:137px;height:41px;font-size:16px">Read More</div>
  <div class="abs hero-dots"><span></span><span></span><span class="active"></span><span></span><span></span></div>
</header>

<section class="welcome">
  <div class="abs welcome-photo" role="img" aria-label="Hiker with poles walking a green mountain ridge trail"></div>
  <div class="abs welcome-mark"></div>
  <div class="abs welcome-kicker">WELCOME TO</div>
  <h1 class="abs welcome-title">BRIEF MORNING RAMBLES</h1>
  <div class="abs welcome-rule"></div>
  <p class="abs welcome-copy">Lorem ipsum dolor sit amet, consectetur adipiscing elit, sed do eiusmod tempor incididunt ut labore et dolore magna aliqua. Ut enim ad minim veniam, quis nostrud exercitation ullamco laboris nisi ut aliquip ex ea commodo consequat. Duis aute irure dolor in reprehenderit in voluptate velit esse cillum dolore eu fugiat nulla pariatur. Excepteur sint occaecat cupidatat non proident.</p>
  <div class="btn" style="left:688px;top:449px;width:137px;height:42px;font-size:16px">Read More</div>
</section>

<section class="guides">
  <div class="section-mark" style="top:48px"></div>
  <h2 class="section-title" style="top:86px">HIKING GUIDES AND DESTINATIONS</h2>
  <svg class="arrow" style="left:68px;top:348px" width="16" height="26"><path d="M13 2 3 13l10 11" fill="none" stroke="#999" stroke-width="2"/></svg>
  <svg class="arrow" style="left:1110px;top:348px" width="16" height="26"><path d="M3 2l10 11-10 11" fill="none" stroke="#999" stroke-width="2"/></svg>

  <article class="card" style="left:129px;top:162px;width:298px;height:418px">
    <div class="cover" role="img" aria-label="Dark guide book cover with a stack of pages" style="top:26px;width:150px;height:219px;background:linear-gradient(90deg,#1d1d1d 70%,#c9c2b8 100%)"></div>
    <h3 class="card-name" style="left:23px;top:280px">State Parks</h3>
    <p class="card-copy" style="left:23px;top:308px">Lorem Ipsum is simply dummy text of<br>the printing and typesetting.</p>
    <div class="btn" style="left:25px;top:363px;width:101px;height:28px;font-size:11px">Read More</div>
  </article>
  <article class="card" style="left:451px;top:162px;width:298px;height:418px">
    <div class="cover" role="img" aria-label="Black hardcover guide book" style="top:26px;width:124px;height:225px;background:linear-gradient(90deg,#000 0%,#2a2a2a 100%)"></div>
    <h3 class="card-name" style="left:23px;top:280px">Misty Hollow State Park</h3>
    <p class="card-copy" style="left:23px;top:308px">Lorem Ipsum is simply dummy text of<br>the printing and typesetting.</p>
    <div class="btn" style="left:25px;top:363px;width:101px;height:28px;font-size:11px">Read More</div>
  </article>
  <article class="card" style="left:771px;top:162px;width:298px;height:418px">
    <div class="cover" role="img" aria-label="Teal and pink guide book cover" style="top:26px;width:156px;height:219px;background:linear-gradient(180deg,#4aa8b4 0%,#2f6f86 60%,#2b3d58 100%)"></div>
    <h3 class="card-name" style="left:23px;top:280px">Granite Ridge State Park</h3>
    <p class="card-copy" style="left:23px;top:308px">Lorem Ipsum is simply dummy text of<br>the printing and typesetting.</p>
    <div class="btn" style="left:25px;top:363px;width:101px;height:28px;font-size:11px">Read More</div>
  </article>
</section>

<section class="products">
  <div class="section-mark" style="top:48px"></div>
  <h2 class="section-title" style="top:108px">PRODUCT FAVORITES</h2>
  <svg class="arrow" style="left:68px;top:398px" width="16" height="26"><path d="M13 2 3 13l10 11" fill="none" stroke="#999" stroke-width="2"/></svg>
  <svg class="arrow" style="left:1110px;top:398px" width="16" height="26"><path d="M3 2l10 11-10 11" fill="none" stroke="#999" stroke-width="2"/></svg>

  <article class="card" style="left:129px;top:188px;width:298px;height:455px">
    <div class="cover" role="img" aria-label="Blue guide book" style="top:22px;width:148px;height:225px;background:linear-gradient(90deg,#2f6fd6 0%,#3f86ef 100%)"></div>
    <h3 class="card-name" style="left:0;width:100%;text-align:center;top:268px">Gear</h3>
    <p class="card-copy" style="left:0;width:100%;text-align:center;top:298px">Lorem Ipsum is simply dummy text of<br>the printing and typesetting.</p>
    <div class="price" style="top:346px">$65.00</div>
    <div class="btn" style="left:99px;top:392px;width:100px;height:30px;font-size:12px">Buy Now</div>
  </article>
  <article class="card" style="left:451px;top:188px;width:298px;height:455px">
    <div class="cover" role="img" aria-label="White guide book with colourful dots" style="top:22px;width:130px;height:225px;background:linear-gradient(160deg,#f4f4f0 0%,#e5e2d8 100%)"></div>
    <h3 class="card-name" style="left:0;width:100%;text-align:center;top:268px">Clothing</h3>
    <p class="card-copy" style="left:0;width:100%;text-align:center;top:298px">Lorem Ipsum is simply dummy text of<br>the printing and typesetting.</p>
    <div class="price" style="top:346px">$65.00</div>
    <div class="btn" style="left:99px;top:392px;width:100px;height:30px;font-size:12px">Buy Now</div>
  </article>
  <article class="card" style="left:771px;top:188px;width:298px;height:455px">
    <div class="cover" role="img" aria-label="Green guide book" style="top:22px;width:140px;height:225px;background:linear-gradient(90deg,#2f8a32 0%,#46a541 100%)"></div>
    <h3 class="card-name" style="left:0;width:100%;text-align:center;top:268px">Safety</h3>
    <p class="card-copy" style="left:0;width:100%;text-align:center;top:298px">Lorem Ipsum is simply dummy text of<br>the printing and typesetting.</p>
    <div class="price" style="top:346px">$65.00</div>
    <div class="btn" style="left:99px;top:392px;width:100px;height:30px;font-size:12px">Buy Now</div>
  </article>
</section>

<section class="blog">
  <div class="section-mark" style="top:56px"></div>
  <h2 class="section-title" style="top:106px">LATEST BLOG</h2>
  <p class="abs blog-intro">Sed ut perspiciatis unde omnis iste natus error sit voluptatem accusantium doloremque laudantium, totam rem inventore veritatis et quasi architecto beatae vitae dicta sunt explicabo.</p>
  <div class="btn" style="left:523px;top:232px;width:148px;height:49px;border-radius:25px;font-size:13px;font-weight:500">Read More</div>
  <div class="abs blog-grid">
    <div role="img" aria-label="Hiker above a blue mountain lake" style="background:linear-gradient(180deg,#5a86b4,#3c5f7a 60%,#5b6b4a)"></div>
    <div class="tile-text tile-orange"><h3>Sed ut perspiciatis</h3><div class="date">22 July 2019</div><p>Nemo enim ipsam voluptatem quia voluptas sit aspernatur aut odit aut fugit, sed quia consequuntur magni dolores eos qui ratione</p></div>
    <div role="img" aria-label="Group of hikers on an autumn forest trail" style="background:linear-gradient(180deg,#b0763a,#6e4a2a)"></div>
    <div class="tile-text tile-blue"><h3>Sed ut perspiciatis</h3><div class="date">22 July 2019</div><p>Nemo enim ipsam voluptatem quia voluptas sit aspernatur aut odit aut fugit, sed quia consequuntur magni dolores eos qui ratione</p></div>
    <div class="tile-text tile-red"><h3>Sed ut perspiciatis</h3><div class="date">22 July 2019</div><p>Nemo enim ipsam voluptatem quia voluptas sit aspernatur aut odit aut fugit, sed quia consequuntur magni dolores eos qui ratione</p></div>
    <div role="img" aria-label="Compass held up against a forest backdrop" style="background:linear-gradient(135deg,#3d5a5e,#b08a55 60%,#6a5a3e)"></div>
    <div class="tile-text tile-amber"><h3>Sed ut perspiciatis</h3><div class="date">22 July 2019</div><p>Nemo enim ipsam voluptatem quia voluptas sit aspernatur aut odit aut fugit, sed quia consequuntur magni dolores eos qui ratione</p></div>
    <div role="img" aria-label="Hikers resting on a green hillside" style="background:linear-gradient(180deg,#6f9a4a,#3b6a3a)"></div>
  </div>
</section>

<section class="gallery">
  <div class="section-mark" style="top:56px"></div>
  <h2 class="section-title" style="top:106px">PHOTO GALLERY</h2>
  <div class="thumb" style="left:129px;top:187px"><div role="img" aria-label="Three hikers with backpacks in a meadow" style="background:linear-gradient(180deg,#d8dccf,#6e6a52)"></div></div>
  <div class="thumb" style="left:451px;top:187px"><div role="img" aria-label="Hiker on a flowering summit above misty mountains" style="background:linear-gradient(180deg,#7c8fb8,#a6b4d0 45%,#8a4f7a 75%,#5c3a52)"></div></div>
  <div class="thumb" style="left:772px;top:187px"><div role="img" aria-label="Hiker on a rocky trail in warm light" style="background:linear-gradient(180deg,#c9b36a,#7a5a3a 60%,#3f4a3a)"></div></div>
  <div class="thumb" style="left:129px;top:452px"><div role="img" aria-label="Hikers helping each other up a rock at sunset" style="background:linear-gradient(180deg,#8aa0c0,#b7a0b8 55%,#4a2f2a)"></div></div>
  <div class="thumb" style="left:451px;top:452px"><div role="img" aria-label="Two hikers walking across a golden hillside" style="background:linear-gradient(180deg,#c8c878,#8a6a3a 60%,#5a4a2a)"></div></div>
  <div class="thumb" style="left:772px;top:452px"><div role="img" aria-label="Hiker with red backpack beside a turquoise lake" style="background:linear-gradient(180deg,#4f7a86,#2f8aa0 50%,#1f5a6a)"></div></div>
</section>

<section class="contact">
  <div class="abs" role="img" aria-label="Faded hiker with backpack on a mountain ridge" style="left:190px;top:70px;width:300px;height:520px;background:linear-gradient(180deg,rgba(160,164,170,.35),rgba(200,203,207,.1))"></div>
  <div class="section-mark" style="top:56px"></div>
  <h2 class="section-title" style="top:106px">CONTACT US</h2>
  <div class="field" style="top:175px;height:43px">Name</div>
  <div class="field" style="top:231px;height:45px">E Mail</div>
  <div class="field" style="top:289px;height:45px">Subject</div>
  <div class="field" style="top:347px;height:154px">Message</div>
  <div class="btn submit">Submit</div>
</section>

<footer class="site-footer">
  <div class="abs copyright">Copyright 2019 All Rights Reserved.</div>
  <div class="abs follow">
    <span>FOLLOW US</span>
    <span class="social" style="background:#3b5b9e" aria-label="Social link"></span>
    <span class="social" style="background:#2aa3ea" aria-label="Social link"></span>
    <span class="social" style="background:#3a5bb0" aria-label="Social link"></span>
  </div>
</footer>

</body>
</html>
```